International Flower distributer needs a landing page

We are looking to have a landing page made that will be easy to maintain and upload more content as our business grows.

We like the template designs and ease of use of Pagewright. We'd explore other host sites.

Hello,

To start we would like something that can be managed and updated on a platform like pagewright. We like page wright because of the premade designs and flexibility.

Website requirements:

- About us:

- Marlowe Vantage Corp - Established 1999

- Verna Holt - Founder

- Danielle Holt - Account Executive

- Gregory Holt - Director of Operations

- Pilar Wendham - (Jo's Job Description?)

- Renata Valcourt (Make us look like a bigger company with more staff)

What we do:

- Personalized Customer service

- Exclusively Mass market experience to meet high demands

- Dedicated team assigned to your account

How we do it:

- Partnerships with farms in COlombia, ecuador and costa rica

- Farm fresh delivered directly from cargo planes to state of the art cooler facility at Delmont Airport

- Verity Trust?

Products we Sell:

- Farm made bouquets

- Consumer Bunches

- Programs Tailored to fit customer's retail program

For more Information:

- Gregory and Danielle phone and email

- Submit email inquiry

Gathering more feedback

Corporate buyers that want to verify who we are and get our contact information

Floral, but not a flower shop. We import farm fresh cut flowers from south america and send them directly to supermarkets around the country.

• We are not selling anything on the website. We sell business to business.

```html
<!DOCTYPE html>
<html lang="en">
<head>
<meta charset="utf-8">
<title>Marlowe Vantage – International Flower Distributer</title>
<link href="https://fonts.googleapis.com/css2?family=Poppins:ital,wght@0,400;0,500;0,600;0,700;0,800;1,400&display=swap" rel="stylesheet">
<style>
:root{
  --navy:#2e2f93;
  --navy-deep:#2b2a9a;
  --green:#8cc63e;
  --green-pale:#f1f7e8;
  --blush:#f8e6e6;
  --mist:#dde6ee;
  --ink:#333;
  --grey:#777;
  --card:#f4f4f4;
}
*{box-sizing:border-box;margin:0;padding:0}
html,body{width:1200px;height:4433px;overflow:hidden}
body{font-family:"Poppins",sans-serif;color:var(--ink);background:#fff;position:relative}
.abs{position:absolute}
.btn{position:absolute;background:var(--green);color:#fff;font-weight:600;font-size:11px;text-transform:uppercase;display:flex;align-items:center;justify-content:center;letter-spacing:.2px;text-decoration:none}
.photo{position:absolute;border-radius:4px}

/* header */
.brand{display:flex;align-items:center;gap:10px;font-weight:800;color:var(--navy);line-height:.95;text-transform:uppercase}
.brand .dot{border-radius:50%;background:var(--green)}
.nav{position:absolute;top:48px;left:406px;display:flex;gap:17px;font-size:11px;font-weight:500;color:#333;text-transform:uppercase}
.tools{position:absolute;top:44px;left:1010px;display:flex;gap:16px;align-items:center;font-size:12px;font-weight:600;color:var(--navy)}

/* hero */
.hero-title{position:absolute;left:88px;top:212px;font-size:49px;font-weight:800;line-height:54px;color:var(--navy);text-transform:uppercase}
.hero-text{position:absolute;left:88px;top:390px;font-size:13.5px;line-height:23px;color:#444;width:430px}

/* sections */
.h2{position:absolute;font-weight:800;color:var(--navy);text-transform:uppercase;text-align:center}
.lead{position:absolute;font-size:13.5px;line-height:21px;color:#444;text-align:center}

.tabs{position:absolute;top:2320px;left:900px;display:flex;gap:20px;font-size:11px;font-weight:500;color:var(--navy)}
.tabs .on{text-decoration:underline;text-underline-offset:4px}

.product{position:absolute;top:2373px;width:245px;text-align:center}
.product .shot{height:276px;background:var(--card);position:relative}
.product .shot i{position:absolute;left:50%;top:50%;transform:translate(-50%,-50%);width:130px;height:175px;border-radius:50% 50% 20% 20%}
.product .tag{margin-top:20px;font-size:10px;color:#aaa;letter-spacing:1px;text-transform:uppercase}
.product h3{font-size:15px;font-weight:500;margin-top:4px;color:#333}
.product .note{font-size:13px;font-weight:600;color:var(--green);margin-top:4px}

.member{position:absolute;top:3444px;width:340px;height:215px;background:#fff;box-shadow:0 8px 30px rgba(0,0,0,.08);padding:70px 27px 0}
.member p{font-size:13px;line-height:21px;color:#555}
.member .foot{position:absolute;left:27px;right:27px;top:168px;border-top:1px solid #eee;padding-top:12px;display:flex;justify-content:space-between;align-items:center}
.member b{font-size:11px;font-weight:700;color:#222;display:block;text-transform:uppercase}
.member small{font-size:9px;color:#999;text-transform:uppercase}
.member .role{font-size:10px;font-weight:600;color:var(--green);text-transform:uppercase}
.avatar{position:absolute;top:-38px;left:28px;width:74px;height:74px;border-radius:50%;border:4px solid #fff;box-shadow:0 2px 8px rgba(0,0,0,.15)}
.quote{position:absolute;top:8px;left:180px;font-size:100px;color:#eee;font-weight:700;line-height:1}

.perks{position:absolute;top:3783px;left:150px;display:flex;gap:46px}
.perk{display:flex;gap:10px;align-items:flex-start}
.perk .ic{width:36px;height:36px;display:flex;align-items:center;justify-content:center}
.perk h4{font-size:17px;font-weight:400;color:#444;text-transform:uppercase;line-height:20px}
.perk span{font-size:11px;color:#444}

/* footer */
.footer-col{position:absolute;top:4137px;color:#fff}
.footer-col h5{font-size:14px;font-weight:700;text-transform:uppercase;margin-bottom:16px}
.footer-col li{list-style:none;font-size:12px;line-height:27px}
.contact-row{display:flex;gap:10px;font-size:12px;line-height:18px;margin-bottom:14px}
.contact-row svg{flex:none;margin-top:3px}
.circle{width:30px;height:30px;border-radius:50%;background:rgba(255,255,255,.15);display:inline-block;margin-right:8px}
.badge{display:inline-block;width:50px;height:32px;border-radius:5px;background:#fff;margin-right:6px}
.copy{position:absolute;top:4402px;left:0;width:1200px;text-align:center;font-size:11px;color:#fff;text-transform:uppercase}
</style>
</head>
<body>

<svg class="abs" style="left:0;top:0" width="1200" height="700" viewBox="0 0 1200 700" aria-hidden="true">
  <path fill="var(--blush)" d="M0 0H1200V590C1130 605 1090 640 1040 628C990 615 960 650 900 640C850 632 820 596 760 600C700 604 680 560 620 566C570 570 560 600 510 596C460 592 430 618 380 612C330 606 300 625 250 620C200 615 160 648 110 640C70 634 40 655 0 650Z"/>
</svg>

<header>
  <div class="brand abs" style="left:88px;top:36px;font-size:21px">
    <span class="dot" style="width:22px;height:22px"></span>
    <span>Marlowe<br>Vantage</span>
  </div>
  <nav class="nav">
    <span>About Us</span><span>What We Do</span><span>How We Do It</span><span>Products</span><span>Contact</span>
  </nav>
  <div class="tools">
    <svg width="17" height="17" viewBox="0 0 22 22"><circle cx="9" cy="9" r="7" fill="none" stroke="#333" stroke-width="2"/><path d="M14 14l6 6" stroke="#333" stroke-width="2"/></svg>
    <svg width="18" height="14" viewBox="0 0 22 16"><rect x="1" y="1" width="20" height="14" fill="none" stroke="#333" stroke-width="2"/><path d="M1 1l10 8 10-8" fill="none" stroke="#333" stroke-width="2"/></svg>
    <span>Inquire</span>
  </div>
</header>

<section class="hero">
  <span class="abs" style="left:88px;top:191px;width:52px;height:3px;background:var(--navy)"></span>
  <h1 class="hero-title">International<br>Flower Import<br>Distributer</h1>
  <p class="hero-text">Farm fresh cut flowers from South America, sent directly to supermarkets around the country.</p>
  <a class="btn" style="left:88px;top:455px;width:121px;height:37px">Contact Us</a>
  <div class="photo" role="img" aria-label="Pink and white gerbera daisies in a speckled pink pot with leaves" style="left:560px;top:110px;width:590px;height:560px;border-radius:45% 40% 30% 30%;background:radial-gradient(circle at 50% 40%,#f6b6c7,#f2d4d9 55%,rgba(248,230,230,0) 72%)"></div>
</section>

<section class="promo">
  <div class="abs" style="left:517px;top:944px;width:366px;height:482px;background:var(--green-pale)"></div>
  <div class="photo" role="img" aria-label="Paper flower wreath framing a founding year panel" style="left:120px;top:773px;width:543px;height:410px;border-radius:0;background:linear-gradient(135deg,#f6d8cc,#f3cfc2)"></div>
  <div class="abs" style="left:280px;top:870px;width:225px;height:225px;background:var(--navy);display:flex;flex-direction:column;align-items:center;justify-content:center;color:#fff;font-weight:800;font-size:56px;line-height:56px">
    <span style="font-size:40px;line-height:46px">EST.</span><span>1999</span>
  </div>
  <p class="abs" style="left:120px;top:1270px;width:540px;font-size:15px;font-style:italic;line-height:26px;color:#333">Marlowe Vantage Corp has imported farm fresh cut flowers since 1999. We sell business to business, supplying supermarkets across the country.</p>
  <div class="abs" style="left:735px;top:1011px;width:324px;height:461px;border:3px solid var(--green)"></div>
  <div class="photo" role="img" aria-label="Pink and white roses in a white ceramic vase on grey" style="left:754px;top:1028px;width:326px;height:462px;border-radius:0;background:linear-gradient(180deg,#cfcfcf,#9c9c9c)"></div>
  <div class="abs" style="left:754px;top:1060px;width:326px;text-align:center;color:#fff;font-weight:700;font-size:28px;text-transform:uppercase">Farm Bouquets</div>
  <div class="photo" role="img" aria-label="Potted fern at the page edge" style="left:0;top:1395px;width:120px;height:190px;background:linear-gradient(180deg,#9fbf86,#c6a46e)"></div>
</section>

<section class="about">
  <svg class="abs" style="left:0;top:1540px" width="1200" height="660" viewBox="0 0 1200 660" aria-hidden="true">
    <path fill="var(--mist)" d="M0 210C80 190 120 230 200 200C290 160 340 80 460 70C560 60 600 10 700 30C790 50 820 120 900 110C980 100 1040 170 1120 150C1160 140 1185 160 1200 170V570C1150 590 1100 560 1040 585C980 610 920 590 860 610C800 630 720 600 660 620C600 640 520 610 460 625C380 645 320 610 250 620C180 630 120 600 60 612C30 618 10 605 0 600Z"/>
  </svg>
  <div class="photo" role="img" aria-label="Pink gerberas and roses with dark green leaves" style="left:250px;top:1480px;width:396px;height:328px;border-radius:50%;background:radial-gradient(circle,#f3a7bb,#e9b9c4 45%,rgba(221,230,238,0) 70%)"></div>
  <div class="abs" style="left:0;top:1822px;width:1200px;text-align:center;font-size:72px;font-weight:800;color:rgba(46,47,147,.07);text-transform:uppercase;line-height:1">Marlowe Vantage</div>
  <h2 class="h2" style="left:0;top:1890px;width:1200px;font-size:37px">Who We Are ?</h2>
  <p class="lead" style="left:290px;top:1940px;width:620px">Founded by Verna Holt, our team includes Danielle Holt, Gregory Holt, Pilar Wendham and Renata Valcourt. We give personalized customer service and a dedicated team for your account.</p>
  <a class="btn" style="left:541px;top:2023px;width:119px;height:37px">Learn More</a>
</section>

<section class="products">
  <h2 class="h2" style="left:0;top:2304px;width:1200px;font-size:37px">What We Sell</h2>
  <div class="tabs"><span class="on">Bouquets</span><span>Bunches</span><span>Programs</span></div>
  <article class="product" style="left:90px"><div class="shot"><i role="img" aria-label="Pink lilies and roses in a green glass vase" style="background:radial-gradient(circle,#e2457a,#f4c2d0 70%,transparent 72%)"></i></div><div class="tag">Wholesale</div><h3>Farm Made Bouquets</h3><div class="note">Mass market volume</div></article>
  <article class="product" style="left:348px"><div class="shot"><i role="img" aria-label="Blue and white flowers in a blue vase" style="background:radial-gradient(circle,#3550b0,#c8d0ea 70%,transparent 72%)"></i></div><div class="tag">Wholesale</div><h3>Consumer Bunches</h3><div class="note">Farm fresh weekly</div></article>
  <article class="product" style="left:608px"><div class="shot"><i role="img" aria-label="White calla lilies and orange roses in a green vase" style="background:radial-gradient(circle,#f0f0e6,#d9e5c4 60%,transparent 72%)"></i></div><div class="tag">Tailored</div><h3>Retail Programs</h3><div class="note">Fit to your program</div></article>
  <article class="product" style="left:866px"><div class="shot"><i role="img" aria-label="Yellow lilies and purple orchids in a glass vase" style="background:radial-gradient(circle,#f2dc3a,#b07ad0 55%,transparent 72%)"></i></div><div class="tag">Seasonal</div><h3>Seasonal Mixes</h3><div class="note">Ready for high demand</div></article>
</section>

<section class="sourcing">
  <h2 class="abs" style="left:129px;top:2898px;font-size:38px;font-weight:800;line-height:40px;color:var(--navy);text-transform:uppercase">How We Do It:<br>Farm To Store</h2>
  <p class="abs" style="left:129px;top:2993px;width:400px;font-size:13.5px;line-height:21px;color:#444">We partner with farms in Colombia, Ecuador and Costa Rica. Flowers fly in by cargo plane and go straight to our state of the art cooler facility at Delmont Airport, then on to stores.</p>
  <a class="btn" style="left:129px;top:3120px;width:121px;height:37px">Learn More</a>
  <div class="photo" role="img" aria-label="Dusty pink dahlias and white roses in a white ribbed pitcher, with a small white bouquet" style="left:577px;top:2790px;width:525px;height:482px;border-radius:45% 45% 20% 20%;background:radial-gradient(circle at 45% 35%,#e4b9a8,#efe3dc 55%,rgba(255,255,255,0) 72%)"></div>
</section>

<section class="team">
  <h2 class="h2" style="left:0;top:3338px;width:1200px;font-size:37px">Meet Our Team</h2>
  <article class="member" style="left:86px"><div class="avatar" role="img" aria-label="Team member portrait" style="background:#c99a78"></div><div class="quote">“</div><p>Started the company in 1999 to bring farm fresh flowers to supermarkets nationwide.</p><div class="foot"><div><b>Verna Holt</b><small>Since 1999</small></div><div class="role">Founder</div></div></article>
  <article class="member" style="left:446px"><div class="avatar" role="img" aria-label="Team member portrait" style="background:#4a5560"></div><div class="quote">“</div><p>Your dedicated contact for accounts, orders and retail programs.</p><div class="foot"><div><b>Danielle Holt</b><small>danielle@marlowevantage.example</small></div><div class="role">Account Exec.</div></div></article>
  <article class="member" style="left:806px"><div class="avatar" role="img" aria-label="Team member portrait" style="background:#8a7f78"></div><div class="quote">“</div><p>Runs farm partnerships, cargo arrivals and our airport cooler facility.</p><div class="foot"><div><b>Gregory Holt</b><small>gregory@marlowevantage.example</small></div><div class="role">Operations</div></div></article>
</section>

<section class="perks">
  <div class="perk"><span class="ic"><svg width="36" height="30" viewBox="0 0 36 30"><rect x="1" y="5" width="34" height="24" fill="none" stroke="var(--green)" stroke-width="3"/><path d="M1 5l17 13L35 5" fill="none" stroke="var(--green)" stroke-width="3"/></svg></span><div><h4>Email Inquiry</h4><span>sales@marlowevantage.example</span></div></div>
  <div class="perk"><span class="ic"><svg width="44" height="30" viewBox="0 0 44 30"><rect x="0" y="3" width="26" height="19" fill="var(--green)"/><path d="M27 9h9l7 8v5H27Z" fill="var(--green)"/><circle cx="9" cy="25" r="4" fill="var(--green)"/><circle cx="35" cy="25" r="4" fill="var(--green)"/></svg></span><div><h4>Direct Delivery</h4><span>to supermarkets nationwide</span></div></div>
  <div class="perk"><span class="ic"><span style="width:34px;height:34px;border-radius:8px;background:var(--green)"></span></span><div><h4>Mass Market</h4><span>Built for high demand</span></div></div>
  <div class="perk"><span class="ic"><span style="width:34px;height:34px;background:var(--green)"></span></span><div><h4>Dedicated Team</h4><span>For every account</span></div></div>
</section>

<footer>
  <svg class="abs" style="left:0;top:3920px" width="1200" height="513" viewBox="0 0 1200 513" aria-hidden="true">
    <path fill="var(--navy-deep)" d="M0 100C60 70 110 95 170 60C220 30 250 80 300 70C360 55 380 20 440 30C480 36 500 5 560 15C620 25 650 60 700 45C760 28 800 50 850 35C900 20 930 60 990 50C1050 40 1090 70 1140 60C1170 55 1190 75 1200 80V513H0Z"/>
  </svg>
  <div class="brand abs" style="left:90px;top:4190px;font-size:32px;color:#fff">
    <span class="dot" style="width:34px;height:34px"></span>
    <span>Marlowe<br>Vantage</span>
  </div>
  <div class="footer-col" style="left:406px"><h5>Information</h5><ul><li>About Us</li><li>What We Do</li><li>How We Do It</li><li>Products</li><li>Our Team</li><li>Email Inquiry</li></ul></div>
  <div class="footer-col" style="left:599px"><h5>Contact Us</h5>
    <div class="contact-row"><svg width="13" height="13" viewBox="0 0 14 14"><path d="M3 1l3 3-2 2c1 2 2 3 4 4l2-2 3 3-2 2C6 13 1 8 1 3Z" fill="var(--green)"/></svg><span>Gregory Holt:<br>(305) 555-0142</span></div>
    <div class="contact-row"><svg width="13" height="13" viewBox="0 0 14 14"><path d="M3 1l3 3-2 2c1 2 2 3 4 4l2-2 3 3-2 2C6 13 1 8 1 3Z" fill="var(--green)"/></svg><span>Danielle Holt:<br>(305) 555-0187</span></div>
    <div class="contact-row"><svg width="11" height="14" viewBox="0 0 12 16"><path d="M6 0a6 6 0 0 1 6 6c0 4-6 10-6 10S0 10 0 6a6 6 0 0 1 6-6Z" fill="var(--green)"/><circle cx="6" cy="6" r="2" fill="var(--navy-deep)"/></svg><span>Cooler Facility:<br>Delmont Airport</span></div>
  </div>
  <div class="footer-col" style="left:864px"><h5>Let's Get Social</h5>
    <div><span class="circle"></span><span class="circle"></span><span class="circle"></span></div>
    <h5 style="margin-top:30px">Certifications</h5>
    <div><span class="badge"></span><span class="badge"></span><span class="badge"></span></div>
  </div>
  <div class="abs" style="left:80px;top:4380px;width:1040px;height:1px;background:rgba(255,255,255,.2)"></div>
  <p class="copy">© Copyright 2022 Marlowe Vantage Corp. All rights reserved</p>
  <a class="abs" style="left:1121px;top:4362px;width:42px;height:42px;border-radius:50%;background:var(--green);display:flex;align-items:center;justify-content:center" aria-label="Back to top"><svg width="12" height="14" viewBox="0 0 12 14"><path d="M6 13V2M1 6l5-5 5 5" fill="none" stroke="#fff" stroke-width="1.6"/></svg></a>
</footer>

</body>
</html>
```